Corvo Grill & Noodle dual-restaurant promotional flyer

I would like to do a tri-fold flyer to promote my two restaurants located close to each other and help concierges understand the subtle differences between them. I have done a mock in powerpoint but it is 300+MB so i took pics of my mock to attach and will attach the separate pictures and text. i would like it put into a proper flyer template and get help to clean up the design, particularly the flyer header which should show either i) our CORVO GRILL and CORVO NOODLE logo or ii) show CORVO logo and then have the words Corvo Grill Corvo Noodle below it (in non-logo). I have the logo files in vector and pdf too if that is better. I need help to photoshop the logos to work with the flyer and clean up overall design. The pages which shows the restaurant contact details is also a little hard to read in the current layout. Open to all changes.

Industry/Entity Type

Restaurant

Requirements
Must have
• Front page - must feature both logos and both restaurants photos (that i show on my uploaded draft flyer)
• All photos must be used
Nice to have
• I have uploaded a draft flyer of what i am trying to achieve
Should not have
• The feel should be warm and personable.

```html
<!DOCTYPE html>
<html lang="en">
<head>
<meta charset="utf-8">
<title>Corvo Grill & Noodle – Tri-fold Flyer</title>
<link rel="stylesheet" href="https://fonts.googleapis.com/css2?family=Arimo:wght@400;700&family=Archivo+Narrow:wght@400;700&display=swap">
<style>
  :root {
    --backdrop: #8a5a36;
    --panel-grey: #a6a7a9;
    --panel-white: #ffffff;
    --ink: #1c1c1c;
    --ink-soft: #333333;
    --charcoal: #2b2b2b;
    --ribbon: #151515;
    --seal-light: #5a5a5a;
    --seal-dark: #262626;
    --seal-text: #9a9a9a;
    --warm-1: #f2a623;
    --warm-2: #b0620f;
    --warm-3: #3a2008;
    --white: #ffffff;
  }
  * { box-sizing: border-box; margin: 0; padding: 0; }
  html, body { width: 1200px; height: 943px; overflow: hidden; }
  body {
    background: var(--backdrop);
    font-family: "Arimo", Arial, sans-serif;
    color: var(--ink);
    position: relative;
  }
  .flyer {
    position: absolute;
    left: 37px; top: 37px;
    width: 1103px; height: 830px;
    transform: scale(1.048);
    transform-origin: 0 0;
    box-shadow: 0 6px 16px rgba(0,0,0,.45);
    display: flex;
  }
  .panel { position: relative; height: 100%; overflow: hidden; }

  /* Panel 1: events */
  .panel--events { width: 357px; background: var(--panel-grey); text-align: center; }
  .photo-party {
    position: absolute; left: -55px; top: -215px;
    width: 370px; height: 525px;
    border-radius: 0 0 50% 50% / 0 0 36% 36%;
    border-bottom-right-radius: 50%;
    background: radial-gradient(circle at 45% 70%, #8c5a48 0%, #4b2c26 45%, #1e1614 100%);
    border: 4px solid var(--white);
  }
  .photo-party { left: -60px; top: -190px; width: 370px; height: 500px; border-radius: 50%; }
  .events-badge {
    position: absolute; left: 191px; top: 213px;
    width: 104px; height: 104px; border-radius: 50%;
    background: radial-gradient(circle at 40% 30%, #4a4a4a, #1e1e1e 70%);
    border: 3px solid var(--white);
    color: var(--white); font-weight: 700; font-size: 21px; line-height: 26px;
    display: flex; align-items: center; justify-content: center;
  }
  .events-intro {
    position: absolute; left: 14px; right: 14px; top: 340px;
    font-family: "Archivo Narrow", Arial, sans-serif; font-size: 12.5px; line-height: 16px;
    color: var(--ink-soft);
  }
  .events-list {
    position: absolute; left: 0; right: 0; top: 419px;
    font-weight: 700; font-size: 15px; line-height: 19px; color: var(--ink-soft);
  }
  .set-lunch { position: absolute; left: 0; right: 0; top: 488px; color: var(--ink-soft); font-size: 20px; line-height: 25px; }
  .set-lunch strong { display: block; }
  .photo-dish {
    position: absolute; left: 87px; top: 565px;
    width: 405px; height: 405px; border-radius: 50%;
    background: radial-gradient(circle at 40% 45%, #e8ecef 0%, #b7c4a0 35%, #6c8a3e 55%, #3a3a36 85%);
    border: 4px solid var(--white);
  }

  /* Panel 2: contacts */
  .panel--contacts { width: 358px; background: var(--panel-white); text-align: center; font-size: 15px; line-height: 19.6px; color: var(--ink); }
  .venue { position: absolute; left: 0; right: 0; }
  .venue--grill { top: 82px; }
  .venue--noodle { top: 475px; }
  .venue-name { font-size: 28px; line-height: 36px; color: var(--ink-soft); margin-bottom: 45px; font-weight: 400; }
  .venue-hours-title { font-weight: 700; margin-top: 20px; }
  .holidays-bar {
    position: absolute; left: 0; right: 0; bottom: 3px; height: 27px;
    background: var(--charcoal); color: var(--white); font-size: 15px; line-height: 27px;
  }

  /* Panel 3: cover */
  .panel--cover { width: 388px; color: var(--white); }
  .photo-interior {
    position: absolute; inset: 0;
    background:
      radial-gradient(ellipse at 75% 35%, var(--warm-1) 0%, var(--warm-2) 35%, transparent 70%),
      linear-gradient(180deg, #c9781a 0%, var(--warm-3) 55%, #0d0805 100%);
  }
  .ribbon { position: absolute; left: 95px; top: 0; }
  .seal {
    position: absolute; left: 35px; top: 65px; width: 290px; height: 165px;
    border-radius: 50%;
    background: radial-gradient(ellipse at 45% 25%, var(--seal-light), var(--seal-dark) 75%);
    border: 2px solid #777;
    display: flex; flex-direction: column; align-items: center; justify-content: center;
    color: var(--seal-text); font-size: 27px; line-height: 44px;
  }
  .cover-copy {
    position: absolute; left: 20px; right: 20px; top: 643px; text-align: center;
    font-family: "Archivo Narrow", Arial, sans-serif; font-size: 14.5px; line-height: 19.5px;
  }
  .cover-copy h2 { font-family: "Arimo", Arial, sans-serif; font-size: 15px; line-height: 19px; font-weight: 700; }
  .award-badge { position: absolute; left: 1025px; top: 772px; }
  .award-badge { left: 310px; }
</style>
</head>
<body>
<main class="flyer">
  <section class="panel panel--events">
    <div class="photo-party" role="img" aria-label="Photo of a group of guests celebrating at a long table inside the restaurant"></div>
    <div class="events-badge">Special<br>Events</div>
    <p class="events-intro">Hold your parties with us! From kids parties to corporate events, Corvo Noodle is the perfect venue to host small gatherings to big groups of up to 120 pax with its airy and cheery indoors and spacious alfresco.</p>
    <p class="events-list">Wine &amp;Apertivo Tastings.<br>Prefix Theatre Dining.<br>Takeaways &amp; Deliveries.</p>
    <p class="set-lunch"><strong>Weekday Set Lunch</strong>$20++ inclusive Coffee &amp; Tea</p>
    <div class="photo-dish" role="img" aria-label="Photo of a set lunch plate with grilled fish, salad, tomatoes and a lemon wedge"></div>
  </section>

  <section class="panel panel--contacts">
    <div class="venue venue--grill">
      <h2 class="venue-name">Corvo Grill</h2>
      <p>18 Marlow Wharf #01-14<br>Singapore 0592716<br>Tel: +65 6100 4821<br>Email: info@corvogrill.com.sg<br>Website: www.corvogrill.com.sg</p>
      <p class="venue-hours-title">Opening Hours:</p>
      <p>Tue, Wed &amp;Thur: 12-3pm, 6-11pm<br>Fri: 12-3pm, 6-11.30pm<br>Sat: 11.30am-3pm, 6-11.30pm<br>Sun: 11.30am-3pm, 6-11pm<br><strong>Closed on Mon</strong></p>
    </div>
    <div class="venue venue--noodle">
      <h2 class="venue-name">Corvo Noodle</h2>
      <p>18 Marlow Wharf #01-09<br>Singapore 0592716<br>Tel: +65 6100-4937<br>Email: Info@corvonoodle.com.sg<br>Website: www.corvonoodle.com.sg</p>
      <p class="venue-hours-title">Opening Hours</p>
      <p>Mon, Wed &amp;Thur: 12-3pm, 6-11pm<br>Fri:&nbsp; 12-3pm, 6-11.30pm<br>Sat: 11.30am-11.30p<br>Sun: 11.30am-11pm<br>Closed on Tue</p>
    </div>
    <div class="holidays-bar">Open on Public Holidays</div>
  </section>

  <section class="panel panel--cover">
    <div class="photo-interior" role="img" aria-label="Photo of the warmly lit restaurant interior at night with diners and a chalkboard menu"></div>
    <svg class="ribbon" width="175" height="300" viewBox="0 0 175 300" aria-hidden="true">
      <polygon points="0,0 175,0 175,268 87.5,232 0,268" fill="var(--ribbon)"/>
    </svg>
    <div class="seal">
      <span>Corvo Grill</span>
      <span>Corvo Noodle</span>
    </div>
    <div class="cover-copy">
      <h2>Two Concepts. One Family.</h2>
      <p>At Corvo Grill, pizzas are the stars while the atmosphere feels cozy and familiar. Whereas Corvo Noodle offers tasty, honest Italian cuisine at arguably the best riverfront spot in Marlow Wharf. Regardless which place you choose, our excellent food and friendly service&nbsp; will surely win hearts.</p>
    </div>
    <svg class="award-badge" width="38" height="43" viewBox="0 0 38 43" aria-hidden="true">
      <rect x="0" y="0" width="38" height="43" fill="var(--white)"/>
      <circle cx="19" cy="20" r="9" fill="none" stroke="#999" stroke-width="1.5"/>
    </svg>
  </section>
</main>
</body>
</html>
```